Pharmacy

Two sided postcard. Pictures on one side. Description on the other. We design and build pharmacies. pictures are some of our finished work. You can use as many pictures as you like not necessary to use all of them. Size of card should be 5"x7". See my website at display@brightfieldfixtures.com for more inspiration. I include the back of one card that I used recently. Both sids need design input. Feel free to contact me with questions.
Requirements
Must have
- Must be a two sided postcard
Nice to have
- I am sending a design of a sleek type postcard that I saw online as an example.
- https://lnk.example-pics.net/images/q7KmRz
- I am looking for something modern.
- Not limited to colors on my website.

```html
<!DOCTYPE html>
<html lang="en">
<head>
<meta charset="utf-8">
<title>Brightfield Display &amp; Store Fixture – Postcard</title>
<link rel="stylesheet" href="https://fonts.googleapis.com/css2?family=Arimo:ital,wght@0,400;0,700;1,400&display=swap">
<style>
  :root {
    --page: #ffffff;
    --tan: #b3a88b;
    --tan-light: #cfc6ad;
    --tan-wash: #a89e84;
    --ink: #1c1c1c;
    --white: #ffffff;
    --photo-dark: #3d3934;
    --photo-mid: #6f675c;
    --photo-light: #cfc9be;
  }
  * { margin: 0; padding: 0; box-sizing: border-box; }
  html, body {
    width: 863px; height: 1200px; overflow: hidden;
    background: var(--page);
    font-family: "Arimo", Arial, sans-serif;
  }
  .canvas { position: relative; width: 863px; height: 1200px; }

  .card {
    position: absolute; left: 118px; width: 660px; height: 470px;
    overflow: hidden; background: var(--white);
  }
  .card--front { top: 70px; }
  .card--back { top: 632px; }

  /* Front */
  .front-photo {
    position: absolute; left: 238px; top: 0; width: 422px; height: 470px;
    background: linear-gradient(160deg, var(--photo-light) 0%, var(--photo-mid) 35%, var(--photo-dark) 60%, #9a948a 85%, #c9c3b8 100%);
  }
  .front-frame {
    position: absolute; left: 26px; top: 28px; width: 610px; height: 416px;
    border: 6px solid var(--tan);
  }
  .front-frame-photo {
    position: absolute; left: 238px; top: 28px; width: 398px; height: 416px;
    border: 5px solid rgba(255,255,255,0.75); border-left: none;
  }
  .front-panel {
    position: absolute; left: 74px; top: 62px; width: 228px; height: 344px;
    background: var(--tan);
  }
  .front-panel .accent-bar {
    position: absolute; left: 0; top: 44px; width: 34px; height: 11px;
    background: var(--white);
  }
  .front-title {
    position: absolute; left: 40px; top: 40px; width: 180px;
    color: var(--white); font-weight: 700; font-size: 17.5px; line-height: 20px;
    text-transform: uppercase; letter-spacing: 0.2px;
  }
  .front-tagline {
    position: absolute; left: 42px; top: 282px; width: 170px;
    color: var(--white); font-style: italic; font-size: 12.5px; line-height: 16px;
  }

  /* Back */
  .back-band {
    position: absolute; left: 0; top: 0; width: 660px; height: 90px;
    background: var(--tan);
  }
  .back-band .accent-bar {
    position: absolute; left: 0; top: 30px; width: 42px; height: 12px;
    background: var(--white);
  }
  .back-title {
    position: absolute; left: 52px; top: 24px;
    color: var(--white); font-size: 17.5px; line-height: 21px;
    text-transform: uppercase; letter-spacing: 0.3px;
  }
  .postage {
    position: absolute; right: 24px; top: 14px;
    color: var(--white); font-size: 9.5px; line-height: 11.5px; text-align: right;
  }
  .back-photo {
    position: absolute; left: 0; top: 90px; width: 660px; height: 380px;
    background: linear-gradient(170deg, #bdb49b 0%, var(--tan-wash) 40%, #8f866e 70%, #a39a81 100%);
  }
  .back-copy {
    position: absolute; left: 42px; top: 90px; width: 262px; height: 380px;
    background: var(--white); color: var(--ink);
  }
  .intro {
    position: absolute; left: 20px; top: 20px; width: 222px;
    font-style: italic; font-size: 13.6px; line-height: 16.6px; text-align: justify;
  }
  .phone {
    position: absolute; left: 0; top: 266px; width: 262px; text-align: center;
    font-weight: 700; font-size: 16px; letter-spacing: 0.3px;
  }
  .contact {
    position: absolute; left: 22px; top: 322px;
    font-size: 12.6px; line-height: 16px;
  }
  .return-address {
    position: absolute; right: 24px; top: 398px;
    color: var(--white); font-weight: 700; font-size: 10.5px; line-height: 12.6px; text-align: right;
  }
</style>
</head>
<body>
<main class="canvas">

  <section class="card card--front" aria-label="Postcard front">
    <div class="front-photo" role="img" aria-label="Photo of a finished pharmacy interior with a white cosmetics counter, a white stool and dark wall shelving"></div>
    <div class="front-frame"></div>
    <div class="front-frame-photo"></div>
    <div class="front-panel">
      <span class="accent-bar"></span>
      <h1 class="front-title">Brightfield Display &amp; Store Fixture Co Inc.</h1>
      <p class="front-tagline">A complete service from design thru installation</p>
    </div>
  </section>

  <section class="card card--back" aria-label="Postcard back">
    <div class="back-band">
      <span class="accent-bar"></span>
      <h2 class="back-title">Brightfield Display<br>&amp; Store Fixture Co. Inc.</h2>
      <p class="postage">presorted<br>FIRST CLASS<br>US POSTAGE<br>PAID<br>Postline</p>
    </div>
    <div class="back-photo" role="img" aria-label="Tan-toned photo of a pharmacy with glass display counters and product shelving"></div>
    <div class="back-copy">
      <p class="intro">Family owned and operated for three generations - Brightfield Display &amp; Store Fixture Co. Inc. is the oldest store fixture company in New Jersey.<br>As designers &amp; manufacturers we can save you hours of time and money. Our level of experience will be evident from the outset and you will be pleased that you found us. We look forward to hearing from you.</p>
      <p class="phone">201 555 0148</p>
      <p class="contact">display@brightfieldfixtures.com<br>www.brightfieldfixtures.com</p>
    </div>
    <p class="return-address">Brightfield display &amp;<br>store fixture co. inc.<br>PO Box 318<br>Ridgefield NJ 07657</p>
  </section>

</main>
</body>
</html>
```